All-Natural Head Lice Removal company

I need a business card with my pre-existing logo. We are a new company located in Portland Oregon that goes into peoples homes to help with head lice removal. My products and approach are all- natural and also will be around children.On my current logo we used Teal Bl and the color Green. I am open to new ideas just want it simple and creative

Target Market(s)

my biggest market is families of school aged children

Industry/Entity Type

Business

Contact Information for Business Card

see upload for details from previous business card

Font styles to use
Serif

Colors
33a6d7
9bcb3b
f37122

Requirements
Must have
• Basic information/ logo put into a creative format that is catching to the eye
Nice to have
• creative

```html
<!DOCTYPE html>
<html lang="en">
<head>
<meta charset="utf-8">
<title>Nitfree Nest – Business Card</title>
<link rel="stylesheet" href="https://fonts.googleapis.com/css2?family=Josefin+Sans:wght@400;600&display=swap">
<style>
  :root {
    --bg: #e2e2e2;
    --paper: #ececec;
    --green: #76ab39;
    --charcoal: #262626;
    --ink: #1e1e1e;
    --white: #ffffff;
  }
  * { margin: 0; padding: 0; box-sizing: border-box; }
  html, body { width: 1200px; height: 900px; overflow: hidden; }
  body {
    background: var(--bg);
    font-family: "Josefin Sans", sans-serif;
    display: flex;
    flex-direction: column;
    align-items: center;
    justify-content: center;
    gap: 40px;
  }
  .card {
    position: relative;
    width: 700px;
    height: 400px;
    background: var(--paper);
    overflow: hidden;
    box-shadow: 0 6px 14px rgba(0,0,0,0.15);
  }
  /* Front */
  .front__band {
    position: absolute;
    left: 0; right: 0;
    height: 58px;
    background: var(--green);
  }
  .front__band--top { top: 0; }
  .front__band--bottom { bottom: 40px; }
  .brand {
    position: absolute;
    left: 0; right: 0; top: 58px; bottom: 98px;
    display: flex;
    align-items: center;
    justify-content: center;
    gap: 16px;
  }
  .brand__dot {
    width: 64px; height: 64px;
    border-radius: 50%;
    background: var(--green);
  }
  .brand__name {
    font-size: 52px;
    font-weight: 600;
    color: var(--ink);
  }
  /* Back */
  .back__shapes { position: absolute; inset: 0; }
  .tagline {
    position: absolute;
    left: 56px; top: 136px;
    font-size: 30px;
    font-weight: 400;
    line-height: 1;
    color: var(--ink);
    white-space: nowrap;
  }
  .person {
    position: absolute;
    left: 400px; top: 212px;
    font-size: 24px;
    font-weight: 600;
    letter-spacing: 1px;
    line-height: 1;
    color: var(--white);
    white-space: nowrap;
  }
  .contact {
    position: absolute;
    left: 60px; top: 232px;
    list-style: none;
    color: var(--white);
    font-size: 16px;
  }
  .contact li {
    display: flex;
    align-items: center;
    gap: 12px;
    margin-bottom: 12px;
    white-space: nowrap;
  }
  .contact svg { width: 16px; height: 16px; fill: none; stroke: var(--white); stroke-width: 1.6; }
</style>
</head>
<body>
  <section class="card card--front">
    <div class="front__band front__band--top"></div>
    <div class="brand">
      <span class="brand__dot"></span>
      <span class="brand__name">Nitfree Nest</span>
    </div>
    <div class="front__band front__band--bottom"></div>
  </section>

  <section class="card card--back">
    <svg class="back__shapes" viewBox="0 0 700 400" aria-hidden="true">
      <polygon points="0,182 380,182 395,176 410,176 355,200 0,200" fill="var(--green)"/>
      <polygon points="0,200 345,200 400,176 700,176 700,400 0,400" fill="var(--charcoal)"/>
      <polygon points="300,284 700,270 700,316 300,332" fill="var(--green)"/>
      <polygon points="670,190 690,222 664,212" fill="var(--green)"/>
    </svg>
    <p class="tagline">All Natural In-Home Lice Removal</p>
    <p class="person">DANA WHITCOMBE</p>
    <ul class="contact">
      <li><svg viewBox="0 0 16 16"><path d="M3 2h3l1 3-2 1.5a8 8 0 0 0 4.5 4.5L11 9l3 1v3a1 1 0 0 1-1 1A11 11 0 0 1 2 3a1 1 0 0 1 1-1z"/></svg>1-855-555 NITS (6487)</li>
      <li><svg viewBox="0 0 16 16"><rect x="1.5" y="3.5" width="13" height="9"/><path d="M1.5 3.5 8 9l6.5-5.5"/></svg>dana@nitfreenest.com</li>
      <li><svg viewBox="0 0 16 16"><circle cx="8" cy="8" r="6.5"/><path d="M1.5 8h13M8 1.5c-3 3.5-3 9.5 0 13M8 1.5c3 3.5 3 9.5 0 13"/></svg>www.nitfreenest.com</li>
    </ul>
  </section>
</body>
</html>
```